Design of Product Brochure

TOV Analytics Consultancy, based in Namibia, is launching a premium charcoal brand: Embera Charcoal. We manufacture two distinct, high-quality product lines: one for the serious home barbecuer and one for professional restaurant kitchens.
The objective of this project is to create a cohesive and compelling visual identity across a product brochure (for B2B sales and high-end B2C) and a marketing website. The designs must elevate Embera Charcoal from a simple commodity to a premium, trusted fuel choice, emphasizing its Namibian origin, scientific backing, and superior performance.

```html
<!DOCTYPE html>
<html lang="en">
<head>
<meta charset="UTF-8">
<title>Embera Charcoal – Brochure Spread</title>
<link rel="stylesheet" href="https://fonts.googleapis.com/css2?family=Montserrat:wght@400;500;700;800&display=swap">
<style>
  :root {
    --backdrop: #e6e6e6;
    --ink-dark: #1c1b1b;
    --ink-deeper: #0f0e0e;
    --ember-red: #d62f2a;
    --ember-orange: #e8702a;
    --text-light: #f2f2f2;
    --text-muted: #c9c9c9;
    --icon-cream: #fbf3ea;
  }
  * { box-sizing: border-box; margin: 0; padding: 0; }
  html, body { width: 1200px; height: 960px; overflow: hidden; }
  body {
    background: var(--backdrop);
    font-family: "Montserrat", sans-serif;
    color: var(--text-light);
    position: relative;
  }
  .spread {
    position: absolute;
    left: 80px; top: 112px;
    width: 1040px; height: 736px;
    display: flex;
    box-shadow: 0 18px 40px rgba(0,0,0,0.25);
  }
  .page { position: relative; width: 520px; height: 736px; overflow: hidden; }

  /* ---------- inside page ---------- */
  .page--about { background: var(--ink-dark); }
  .briquette-photo {
    position: absolute; inset: 0;
    background:
      radial-gradient(ellipse 45% 30% at 55% 38%, rgba(232,112,42,0.35), transparent 70%),
      radial-gradient(ellipse 50% 28% at 50% 62%, rgba(214,47,42,0.3), transparent 70%),
      linear-gradient(180deg, #1e1d1d 0%, #262220 45%, #1d1b1a 100%);
  }
  .about-content { position: absolute; inset: 0; padding: 70px 44px 40px; }

  .intro-quote {
    position: relative;
    font-size: 15px; line-height: 1.35; font-weight: 400;
    padding-left: 22px; max-width: 400px;
  }
  .intro-quote strong { font-weight: 700; }
  .intro-quote .mark { color: var(--ember-red); font-weight: 800; font-size: 22px; line-height: 1; }
  .intro-quote .mark--open { position: absolute; left: 0; top: -2px; }
  .intro-quote .mark--close { margin-left: 6px; vertical-align: -6px; }

  .section-head { display: flex; align-items: center; gap: 12px; margin-bottom: 10px; }
  .section-title { font-size: 15px; font-weight: 800; letter-spacing: 0.5px; white-space: nowrap; }
  .rule { flex: 1; height: 1px; background: var(--ember-red); }
  .rule--full { height: 1px; background: var(--ember-red); margin: 22px 0; }

  .about-us { margin-top: 40px; }
  .two-col { display: grid; grid-template-columns: 1fr 1fr; column-gap: 26px; }
  .body-text { font-size: 9.5px; line-height: 1.45; color: var(--text-muted); }

  .core-values { margin-top: 28px; }
  .value { display: flex; gap: 12px; align-items: flex-start; margin-bottom: 12px; }
  .value-icon {
    flex: 0 0 34px; height: 34px; border-radius: 50%;
    background: var(--icon-cream);
    border: 3px solid rgba(232,112,42,0.35);
  }
  .value-name { font-size: 9.5px; font-weight: 700; text-transform: uppercase; margin-bottom: 2px; }
  .value-text { font-size: 9px; line-height: 1.4; color: var(--text-muted); }

  .contact-grid { display: grid; grid-template-columns: 1fr 1fr 1fr; column-gap: 14px; row-gap: 14px; margin-top: 6px; }
  .contact-line { display: flex; align-items: center; gap: 7px; font-size: 9.5px; }
  .contact-icon {
    flex: 0 0 16px; height: 16px; border-radius: 50%;
    background: var(--ember-red); display: grid; place-items: center;
  }
  .office-name { font-size: 9.5px; font-weight: 700; text-transform: uppercase; }
  .office-address { font-size: 9px; line-height: 1.4; color: var(--text-muted); }

  /* ---------- cover page ---------- */
  .page--cover { background: var(--ink-deeper); }
  .grill-photo {
    position: absolute; inset: 0;
    background:
      radial-gradient(ellipse 40% 22% at 48% 40%, rgba(176,92,52,0.55), transparent 70%),
      radial-gradient(ellipse 30% 14% at 62% 56%, rgba(224,120,50,0.45), transparent 70%),
      linear-gradient(170deg, #5a3c2c 0%, #2b2a2e 20%, #1c1d22 48%, #141313 78%, #0c0c0c 100%);
  }
  .cover-brand { position: absolute; left: 0; right: 0; bottom: 110px; text-align: center; }
  .brand-lockup { display: inline-flex; align-items: center; gap: 12px; margin-bottom: 14px; }
  .brand-dot { width: 30px; height: 30px; border-radius: 50%; background: var(--ember-red); }
  .brand-name { font-size: 22px; font-weight: 800; letter-spacing: 1px; color: var(--text-light); }
  .cover-tagline { font-size: 19px; font-weight: 800; letter-spacing: 0.5px; }
  .cover-promise { font-size: 17px; font-weight: 400; line-height: 1.3; margin-top: 4px; }
</style>
</head>
<body>
<main class="spread">

  <!-- inside page -->
  <section class="page page--about">
    <div class="briquette-photo" role="img" aria-label="Glowing hardwood charcoal briquettes with orange embers"></div>
    <div class="about-content">
      <p class="intro-quote">
        <span class="mark mark--open">&ldquo;</span>From the heart of Southern Africa to your grill <strong>premium hardwood charcoal</strong> with unmatched performance and sustainability.<span class="mark mark--close">&rdquo;</span>
      </p>

      <div class="about-us">
        <div class="section-head">
          <h2 class="section-title">ABOUT US</h2><span class="rule"></span>
        </div>
        <div class="two-col">
          <p class="body-text">TOV Analytics Consultancy and Trading was established in 2016 with a vision to become a leading player in the global commodity trading market, specializing in biomass products. With a strategic focus on manufacturing high-quality charcoal products, the company has</p>
          <p class="body-text">rapidly grown to serve both consumer and commercial markets. TOV operates out of Namibia, Cape Town, and Johannesburg, leveraging the rich natural resources of Southern Africa to produce premium hardwood charcoal.</p>
        </div>
      </div>

      <div class="core-values">
        <div class="section-head">
          <h2 class="section-title">CORE VALUES</h2>
        </div>
        <div class="two-col">
          <div>
            <div class="value"><span class="value-icon"></span><div><h3 class="value-name">Quality</h3><p class="value-text">Ensuring the highest standards in all our products and services.</p></div></div>
            <div class="value"><span class="value-icon"></span><div><h3 class="value-name">Customer Focus</h3><p class="value-text">Prioritizing customer satisfaction and building long-term relationships.</p></div></div>
            <div class="value"><span class="value-icon"></span><div><h3 class="value-name">Innovation</h3><p class="value-text">Continuously improving and innovating our products and processes.</p></div></div>
          </div>
          <div>
            <div class="value"><span class="value-icon"></span><div><h3 class="value-name">Sustainability</h3><p class="value-text">Committing to environmentally friendly practices and sustainable sourcing.</p></div></div>
            <div class="value"><span class="value-icon"></span><div><h3 class="value-name">Integrity</h3><p class="value-text">Conducting our business with honesty and transparency.</p></div></div>
          </div>
        </div>
      </div>

      <div class="rule--full"></div>

      <div class="get-in-touch">
        <div class="section-head">
          <h2 class="section-title">GET IN TOUCH</h2>
        </div>
        <div class="contact-grid">
          <div class="contact-line">
            <span class="contact-icon"><svg width="9" height="9" viewBox="0 0 24 24"><path fill="#fff" d="M6.6 10.8a15 15 0 0 0 6.6 6.6l2.2-2.2c.3-.3.7-.4 1-.2 1.1.4 2.3.6 3.6.6.6 0 1 .4 1 1V20c0 .6-.4 1-1 1A17 17 0 0 1 3 4c0-.6.4-1 1-1h3.5c.6 0 1 .4 1 1 0 1.3.2 2.5.6 3.6.1.3 0 .7-.2 1z"/></svg></span>
            +264 61 480 317
          </div>
          <div class="contact-line">
            <span class="contact-icon"><svg width="10" height="10" viewBox="0 0 24 24" fill="none" stroke="#fff" stroke-width="2"><circle cx="12" cy="12" r="9"/><path d="M3 12h18M12 3c3 3 3 15 0 18M12 3c-3 3-3 15 0 18"/></svg></span>
            www.tovanalytics.com.na
          </div>
          <div class="contact-line">
            <span class="contact-icon"><svg width="10" height="10" viewBox="0 0 24 24" fill="none" stroke="#fff" stroke-width="2"><rect x="3" y="5" width="18" height="14" rx="1"/><path d="M3 6l9 7 9-7"/></svg></span>
            info@tovanalytics.com.na
          </div>
          <div>
            <h3 class="office-name">Headquarter</h3>
            <p class="office-address">12, Kalahari Court,<br>Acacia Street,<br>Windhoek, Namibia</p>
          </div>
          <div>
            <h3 class="office-name">SA Office</h3>
            <p class="office-address">58 Harbour Lane,<br>Seaview Office Park,<br>Muizenberg, Cape Town</p>
          </div>
        </div>
      </div>
    </div>
  </section>

  <!-- cover page -->
  <section class="page page--cover">
    <div class="grill-photo" role="img" aria-label="Meat grilling over charcoal on an outdoor barbecue grate, tended by a hand"></div>
    <div class="cover-brand">
      <div class="brand-lockup">
        <span class="brand-dot"></span>
        <span class="brand-name">EMBERA CHARCOAL</span>
      </div>
      <p class="cover-tagline">ORGANIC FIRE</p>
      <p class="cover-promise">for uncompromising performance<br>and flavour.</p>
    </div>
  </section>

</main>
</body>
</html>
```